Flyer für Mobile Massage am Arbeitsplatz
Zielgruppe
Der Flyer richtet sich an Geschäftsleitungen, Firmenvorstände, Betriebsräte.
Ich werde den Flyer sowohl persönlich überreichen, als auch postalisch verschicken.
Aufgabenstellung
Es geht um einen Flyer, DIN lang, Hochformat, beidseitig bedruckt.

```html
<!DOCTYPE html>
<html lang="de">
<head>
<meta charset="utf-8">
<title>Mobile Massage am Arbeitsplatz – Flyer DIN lang</title>
<link rel="stylesheet" href="https://fonts.googleapis.com/css2?family=Source+Sans+3:wght@400;600&family=Noto+Serif:wght@400;700&display=swap">
<style>
  :root {
    --page-bg: #e9e6e1;
    --paper: #ffffff;
    --swoosh-dark: #c9c7c5;
    --swoosh-light: #f1f0ef;
    --ink: #1e1e1e;
    --ink-soft: #4a4a4a;
    --title: #3a3a3a;
    --photo-dark: #8f8a84;
    --photo-light: #e4e2df;
  }
  * { box-sizing: border-box; margin: 0; padding: 0; }
  html, body { width: 1200px; height: 900px; overflow: hidden; }
  body {
    background: var(--page-bg);
    position: relative;
    font-family: "Noto Serif", Georgia, serif;
    color: var(--ink);
  }
  .flyer {
    position: absolute;
    top: 50px;
    width: 380px;
    height: 800px;
    background: var(--paper);
    overflow: hidden;
    box-shadow: 0 4px 14px rgba(0,0,0,.18);
  }
  .flyer--front { left: 190px; }
  .flyer--back { left: 630px; }
  .flyer__swoosh { position: absolute; inset: 0; width: 100%; height: 100%; }
  .flyer__content { position: absolute; inset: 0; }

  .front__title {
    position: absolute; left: 0; right: 0; top: 52px;
    text-align: center;
    font-family: "Source Sans 3", Arial, sans-serif;
    color: var(--title);
    font-weight: 400;
    line-height: 1.1;
  }
  .front__title-main { display: block; font-size: 37px; }
  .front__title-sub { display: block; font-size: 29px; letter-spacing: 1.5px; margin-top: 4px; }
  .phone {
    position: absolute;
    font-family: "Source Sans 3", Arial, sans-serif;
    color: var(--ink-soft);
    letter-spacing: 2px;
  }
  .front__phone { left: 0; right: 0; top: 148px; text-align: center; font-size: 25px; }
  .back__phone { left: 70px; top: 60px; font-size: 23px; }

  .photo {
    position: absolute;
    background: radial-gradient(ellipse at 50% 45%, var(--photo-dark) 0%, #b3afaa 45%, var(--photo-light) 78%, rgba(255,255,255,0) 100%);
  }
  .front__photo { left: 45px; top: 250px; width: 290px; height: 510px; }
  .back__photo { left: 240px; top: 555px; width: 125px; height: 215px; }

  .web {
    position: absolute; left: 0; right: 0; bottom: 22px;
    text-align: center;
    font-size: 14px;
    color: var(--ink);
  }

  .back__text {
    position: absolute; left: 30px; width: 315px; top: 120px;
    font-size: 13.5px; line-height: 1.38;
  }
  .back__text p { margin-bottom: 14px; }
  .back__text strong { font-weight: 700; }
  .prices {
    position: absolute; left: 30px; top: 555px;
    font-size: 15px; line-height: 1.35;
  }
  .prices__label { margin-bottom: 22px; }
  .prices strong { font-weight: 700; }
  .tax-note {
    position: absolute; left: 30px; top: 712px; width: 195px;
    font-size: 10px; line-height: 1.3; color: var(--ink-soft);
  }
</style>
</head>
<body>

<section class="flyer flyer--front">
  <svg class="flyer__swoosh" viewBox="0 0 380 800" preserveAspectRatio="none" aria-hidden="true">
    <defs>
      <linearGradient id="swooshFront" x1="0" y1="0" x2="1" y2="1">
        <stop offset="0" stop-color="var(--swoosh-dark)"/>
        <stop offset=".6" stop-color="var(--swoosh-light)"/>
        <stop offset="1" stop-color="var(--swoosh-dark)"/>
      </linearGradient>
    </defs>
    <rect width="380" height="800" fill="url(#swooshFront)"/>
    <path d="M60 0 H380 V480 C350 650 230 740 60 770 C40 560 20 260 60 0 Z" fill="var(--paper)"/>
    <path d="M0 740 C120 760 260 700 380 600 V800 H0 Z" fill="#dcdad8"/>
    <rect x="0" y="755" width="380" height="45" fill="var(--paper)"/>
  </svg>
  <div class="flyer__content">
    <h1 class="front__title">
      <span class="front__title-main">Mobile Massage</span>
      <span class="front__title-sub">am Arbeitsplatz</span>
    </h1>
    <p class="phone front__phone">Tel.: 030 - 48213907</p>
    <div class="photo front__photo" role="img" aria-label="Foto: Masseur behandelt einen Mann im Anzug auf einem gelben Massagestuhl"></div>
    <p class="web">www.massage-im-buero-havelland.de</p>
  </div>
</section>

<section class="flyer flyer--back">
  <svg class="flyer__swoosh" viewBox="0 0 380 800" preserveAspectRatio="none" aria-hidden="true">
    <defs>
      <linearGradient id="swooshBack" x1="1" y1="0" x2="0" y2="1">
        <stop offset="0" stop-color="var(--swoosh-dark)"/>
        <stop offset=".55" stop-color="var(--swoosh-light)"/>
        <stop offset="1" stop-color="var(--swoosh-dark)"/>
      </linearGradient>
    </defs>
    <rect width="380" height="800" fill="url(#swooshBack)"/>
    <path d="M0 0 H310 C370 200 370 450 300 560 C250 640 160 690 0 720 Z" fill="var(--paper)"/>
    <rect x="0" y="755" width="380" height="45" fill="var(--paper)"/>
  </svg>
  <div class="flyer__content">
    <p class="phone back__phone">Tel.: 030 - 48213907</p>
    <div class="back__text">
      <p>In unseren Massagen am Arbeitsplatz lassen wir Elemente aus der <strong>Shiatsu - Energiemassage</strong> und den <strong>Joint Release - Gelenklockerungen</strong> zusammenfließen.</p>
      <p>Auf diese Weise eröffnen wir einen Raum für spürbare <strong>Entspannung</strong> mitten im Arbeitsalltag. Die Massagen befreien aus berufsbedingten <strong>Zwangshaltungen</strong>, wirken stresslindernd und stimmungshebend im team, fokussieren auf die Problemzonen im Büro:</p>
      <p><strong>Rücken, Nacken, Schulter</strong> und <strong>Maushand</strong> und sind ein Baustein im innerbetrieblichen Gesundheitsmanagement.</p>
    </div>
    <div class="prices">
      <p class="prices__label">Preise:</p>
      <p><strong>20 Minuten : 16 Euro</strong><br>inklusive Anfahrt<br>buchbar ab <strong>4 Personen</strong></p>
    </div>
    <div class="photo back__photo" role="img" aria-label="Foto: Masseur behandelt einen Mann auf einem gelben Massagestuhl"></div>
    <p class="tax-note">Die Kosten können, sofern vom Arbeitgeber getragen, nach §3 Nr.34 EStG von der Steuer abgesetzt werden.</p>
    <p class="web">www.massage-im-buero-havelland.de</p>
  </div>
</section>

</body>
</html>
```